Discreet simple classy for adult entertainment

I would like a matte black business card with gold writing for my business. Keeping it simple. Having my following:

Lana frost
Events. Entertainment. Promotions
0491726580

or alternatively could have what i had on my previous card below but i think i prefer the above as again - discretion.

Maybe a nice gold line thru the card or some other very simple design . Or not open to ideas/ can be doublesided if any good ideas with that.

included pics of my old bus card. not sure weather i want a photo on it or not. if i do it wont be the same pic. i kinda wanted a card that was discreet so if it was in someones wallet they wouldn't neccessarily realise it was from a stripper.

Target Market(s)

men

Industry/Entity Type

Business

Contact Information for Business Card

Lana frost
0491726580

Requirements
Nice to have
• i don't know i am really open to anything. im giving my cards to guys so something they can have in their wallet that is discreet preferably.

```html
<!DOCTYPE html>
<html lang="en">
<head>
<meta charset="UTF-8">
<title>Lana Frost — Business Card</title>
<link href="https://fonts.googleapis.com/css2?family=Barlow:wght@400;500&display=swap" rel="stylesheet">
<style>
  :root {
    --backdrop: #2a2c2e;
    --card-black: #151515;
    --gold: #b59b5c;
  }
  html, body {
    margin: 0;
    padding: 0;
    width: 1200px;
    height: 800px;
    overflow: hidden;
    background: var(--backdrop);
  }
  .business-card {
    position: absolute;
    left: 75px;
    top: 100px;
    width: 1050px;
    height: 600px;
    background: var(--card-black);
    font-family: "Barlow", sans-serif;
    color: var(--gold);
  }
  .card-frame {
    position: absolute;
    inset: 22px;
    border: 2px solid var(--gold);
  }
  .brand-name {
    position: absolute;
    left: 215px;
    top: 118px;
    margin: 0;
    font-size: 118px;
    font-weight: 400;
    letter-spacing: 6px;
    line-height: 1;
    white-space: nowrap;
  }
  .services {
    position: absolute;
    left: 195px;
    top: 248px;
    width: 650px;
    margin: 0;
    padding-bottom: 8px;
    border-bottom: 2px solid var(--gold);
    font-size: 29px;
    font-weight: 400;
    letter-spacing: 1.5px;
    line-height: 1;
    white-space: nowrap;
  }
  .phone-number {
    position: absolute;
    left: 280px;
    top: 345px;
    width: 300px;
    margin: 0;
    text-align: center;
    font-size: 29px;
    font-weight: 400;
    letter-spacing: 1px;
    line-height: 1;
  }
  .phone-marker {
    position: absolute;
    left: 410px;
    top: 398px;
    width: 40px;
    height: 182px;
  }
</style>
</head>
<body>
  <div class="business-card">
    <div class="card-frame"></div>
    <h1 class="brand-name">LANA FROST</h1>
    <p class="services">EVENTS | ENTERTAINMENT | PROMOTIONS</p>
    <p class="phone-number">(049)-172-6580</p>
    <svg class="phone-marker" viewBox="0 0 40 182" aria-hidden="true">
      <circle cx="20" cy="20" r="17" fill="none" stroke="#b59b5c" stroke-width="2"/>
      <path d="M14.5 11.5c1-.6 2-.3 2.5.6l1.4 2.8c.4.8.2 1.7-.5 2.2l-1.2.9c.8 2 2.4 3.9 4.3 5l1.1-1c.7-.6 1.6-.7 2.3-.2l2.6 1.7c.8.6 1 1.6.4 2.5l-.9 1.3c-.8 1.1-2.2 1.6-3.5 1.1-4.6-1.8-8.4-5.8-10-10.5-.4-1.3.1-2.7 1.2-3.5z" fill="#b59b5c"/>
      <line x1="20" y1="37" x2="20" y2="182" stroke="#b59b5c" stroke-width="2"/>
    </svg>
  </div>
</body>
</html>
```